Pawn Shop Website

I want my site to be similar to quillbarter.net. Except, I will not be selling anything off the site. Would rather it just be informational. I have a logo which I would like to use.

Also, I do not need this site to be perfect. I will do a lot of altering myself and I would typically design the entire page myself but am overwhelmed with other responsibilities. Plus, you guys are great here and i've used this service before and you really give great ideas. So, I'm just looking for a template. I can handle making a flash banner, but it will give you kudos points if included.
Updates

Also, I want the colors to be Gray and Black for background.  Then for the fonts Gold inside and Green outline.  I will be posting the information for my logo once I get to my other computer.

Industry/Entity Type

Shop

Requirements
Must have
• Main location
4127 W Hollister Ave
Harlow Ridge, IL 60892
555-862-1937

other location
Brindle Cove Pawn Shop
2805 E Fenwick St.
Ferncliff, IL 60847
555-317-4086

```html
<!DOCTYPE html>
<html lang="en">
<head>
<meta charset="utf-8">
<title>Gilded Anchor Pawn</title>
<link href="https://fonts.googleapis.com/css2?family=Ropa+Sans&family=Open+Sans:ital,wght@0,400;0,700;1,400&display=swap" rel="stylesheet">
<style>
:root{
  --bg:#1c1c1c;
  --panel:#000;
  --panel-edge:#3a3a3a;
  --gold:#f2c21e;
  --gold-deep:#e0a812;
  --text-gold:#e2b524;
  --green:#b9ec52;
  --green-glow:#5fae1c;
  --white:#f4f4f4;
  --rule:#4a3f12;
}
*{margin:0;padding:0;box-sizing:border-box}
html,body{width:931px;height:1200px;overflow:hidden;background:var(--bg)}
body{position:relative;font-family:"Open Sans",sans-serif;color:var(--text-gold)}
.abs{position:absolute}
.heading{font-family:"Ropa Sans",sans-serif;font-weight:400;color:var(--green);font-size:17px;white-space:nowrap}

.site-header{left:0;top:0;width:931px;height:145px;background:linear-gradient(#0c0c0c,#222 90%,#2c2c2c)}
.top-links{right:24px;top:18px;font-size:11px;font-weight:700;color:var(--gold)}
.top-links span{margin:0 5px}
.brand{left:30px;top:56px;display:flex;align-items:center;gap:10px}
.brand-mark{width:22px;height:22px;border-radius:50%;background:var(--gold)}
.brand-name{font-family:"Ropa Sans",sans-serif;font-weight:400;font-size:34px;color:var(--gold);line-height:1}
.search{left:665px;top:92px;width:245px;height:29px;border-radius:15px;background:#3a3a3a;display:flex;align-items:center;padding-left:15px;font-size:10px;color:#9a9a9a}
.search-go{position:absolute;right:0;top:0;width:29px;height:29px;border-radius:50%;background:var(--gold);color:#111;font-weight:700;font-size:11px;display:flex;align-items:center;justify-content:center}

.main-nav{left:0;top:145px;width:931px;height:54px;background:linear-gradient(#f6cf2e,#e9b414);border-top:2px solid var(--green-glow)}
.main-nav .item{position:absolute;top:0;height:54px;line-height:52px;transform:translateX(-50%);font-family:"Ropa Sans",sans-serif;font-weight:400;font-size:16px;color:#1a1a1a;white-space:nowrap}
.main-nav .active{left:32px;width:70px;transform:none;text-align:center;background:#221f18;color:var(--white)}

.panel{background:var(--panel);border:1px solid var(--panel-edge)}
.panel-head{position:absolute;left:0;width:100%;height:38px;background:linear-gradient(#2a2a2a,#0e0e0e);padding:9px 0 0 14px}

.category-list{left:9px;top:256px;width:185px;list-style:none}
.category-list li{height:22.7px;line-height:22px;border-bottom:1px solid #2c2c2c;padding-left:26px;font-size:10px;font-weight:700;color:var(--gold);background:#060606}
.info-list{left:30px;top:545px;list-style:none}
.info-list li{height:23px;font-size:10px;color:var(--gold)}
.info-list li::before,.quick-links li::before{content:"";display:inline-block;border-left:4px solid var(--gold);border-top:3px solid transparent;border-bottom:3px solid transparent;margin-right:7px;vertical-align:1px}
.quote{left:21px;top:724px;width:160px;font-size:10px;font-style:italic;line-height:16.4px;color:var(--gold-deep)}
.quote-author{left:23px;top:826px;font-size:10px;font-weight:700;color:var(--gold)}

.banner{left:211px;top:222px;width:504px;height:208px;background:radial-gradient(ellipse at 50% 55%,#3a7e4e 0,#c84040 30%,#e8e8e8 62%,#fafafa 100%)}
.welcome-text{left:222px;top:466px;width:482px;font-size:9.8px;line-height:15.6px;color:var(--text-gold)}
.rule{left:221px;top:557px;width:487px;height:1px;background:var(--rule)}
.new-bar{left:221px;top:574px;width:487px;height:36px;background:linear-gradient(#242424,#0d0d0d);border:1px solid #3a3a3a;padding:6px 0 0 15px}
.product{width:103px;height:107px;border:3px solid #e8e8e8}
.product-name{font-size:10px;color:var(--gold)}

.about-text{left:748px;top:260px;width:165px;font-size:9.6px;line-height:15.6px;color:var(--gold-deep)}
.read-more{left:751px;top:432px;font-size:10px;color:var(--gold)}
.special{width:74px;height:57px;border:2px solid #e8e8e8}
.special-name{font-family:"Ropa Sans",sans-serif;font-weight:400;font-size:13px;color:var(--gold)}
.special-desc{font-size:10px;line-height:15.4px;color:var(--gold-deep);width:100px}

.site-footer{left:0;top:946px;width:931px;height:208px;background:#1f1f1f}
.quick-links{list-style:none;font-size:11px;color:var(--gold)}
.quick-links li{height:25.4px}
.store{font-family:"Ropa Sans",sans-serif;font-weight:400;font-size:12.5px;color:var(--gold);line-height:22.7px;white-space:nowrap}
.copyright-bar{left:0;top:1154px;width:931px;height:46px;background:#0a0a0a;border-top:1px solid #2a2a2a}
.copyright{left:25px;top:1170px;font-size:11px;color:var(--gold)}
.copyright span{margin:0 6px;color:#777}
</style>
</head>
<body>

<header class="site-header abs">
  <div class="top-links abs">My Account<span>|</span>FAQ's<span>|</span>Contact<span>|</span>Sitemap</div>
  <div class="brand abs"><div class="brand-mark"></div><div class="brand-name">Gilded Anchor Pawn</div></div>
  <div class="search abs">Enter you word<div class="search-go">Go</div></div>
</header>

<nav class="main-nav abs">
  <span class="item active">Main</span>
  <span class="item" style="left:154px">About Us</span>
  <span class="item" style="left:251px">Products</span>
  <span class="item" style="left:344px">Services</span>
  <span class="item" style="left:450px">Testimonials</span>
  <span class="item" style="left:568px">Recent Blog</span>
  <span class="item" style="left:671px">Sitemap</span>
  <span class="item" style="left:764px">Location</span>
  <span class="item" style="left:855px">Contact</span>
</nav>

<aside class="panel abs" style="left:9px;top:216px;width:186px;height:722px">
  <div class="panel-head heading" style="top:0">Select Category</div>
  <div class="panel-head heading" style="top:282px">Information</div>
  <div class="panel-head heading" style="top:456px">Testimonials</div>
</aside>
<ul class="category-list abs">
  <li>AMPLIFIERS &amp; SPEAKERS</li><li>GUITARS &amp; BASSES 2</li><li>PEDALS &amp; KEYBOARDS</li>
  <li>DRUMS &amp; PERCUSSION</li><li>HOME &amp; ELECTRONICS 3</li><li>JEWELRY &amp; WATCHES</li>
  <li>CAR AUDIO 1</li><li>HOBBIES &amp; SPORTS</li><li>TOOLS &amp; VEHICLES</li><li style="border:0">ALL PRODUCTS...</li>
</ul>
<ul class="info-list abs">
  <li>Privacy Notice</li><li>Conditions of Use</li><li>Site Map</li><li>Discount Coupons</li><li>Newsletter Unsubscribe</li>
</ul>
<p class="quote abs">Our Website Design team give an unforgettable impression on the customers and the clients. We can assure you that this is the best place for requirement of yours regarding website design solutions</p>
<div class="quote-author abs" style="top:829px">BY AUTHOR NAME</div>

<main class="panel abs" style="left:205px;top:216px;width:518px;height:722px"></main>
<div class="banner abs" role="img" aria-label="Collection of promotional goods: bags, bottles, pens and small gifts"></div>
<h1 class="heading abs" style="left:222px;top:441px">Welcome to Our Website Mainpage</h1>
<p class="welcome-text abs">Brightweave Studio is a web service company, offering a wide range of services which range from designing and development, that is covering almost all the fields in the best possible way. To be the best we know what and how to present beautifully the working of the client's need and their advantages be highlighted. We act in accordance with the Industry certified processes to deliver the best to our clients all over the world.</p>
<div class="rule abs"></div>
<div class="new-bar abs heading">New Products</div>

<div class="product abs" style="left:223px;top:623px;background:linear-gradient(135deg,#f4d6e0,#e8a6c0 50%,#fff)" role="img" aria-label="Cosmetics set"></div>
<div class="product abs" style="left:344px;top:623px;background:linear-gradient(#1e1e1e,#5c6a7a 60%,#eee)" role="img" aria-label="Smartphone"></div>
<div class="product abs" style="left:469px;top:623px;background:radial-gradient(circle at 50% 60%,#555,#bbb 45%,#fff 70%)" role="img" aria-label="Steam cleaner"></div>
<div class="product abs" style="left:592px;top:623px;background:linear-gradient(90deg,#fff,#3b3a86 25%,#9a9aa4 55%,#a2652a 80%,#fff)" role="img" aria-label="Metal water bottles"></div>
<div class="product abs" style="left:223px;top:775px;background:radial-gradient(circle at 50% 60%,#2a3fc0,#5aa0d8 50%,#fff 75%)" role="img" aria-label="Basket of cleaning supplies"></div>
<div class="product abs" style="left:344px;top:775px;background:radial-gradient(circle at 50% 50%,#e08a2a,#777 45%,#fff 75%)" role="img" aria-label="Travel bag"></div>
<div class="product abs" style="left:469px;top:775px;background:linear-gradient(90deg,#fff,#3a7a3a 20%,#b02a2a 45%,#2a4a9a 70%,#fff)" role="img" aria-label="Assorted drink bottles and mugs"></div>
<div class="product abs" style="left:592px;top:775px;background:radial-gradient(circle at 55% 50%,#444,#1a1a1a 40%,#bbb 60%,#fff 80%)" role="img" aria-label="Compact digital camera"></div>
<div class="product-name abs" style="left:223px;top:736px">Product Name</div>
<div class="product-name abs" style="left:344px;top:736px">Product Name</div>
<div class="product-name abs" style="left:469px;top:736px">Product Name</div>
<div class="product-name abs" style="left:594px;top:736px">Product Name</div>
<div class="product-name abs" style="left:224px;top:891px">Product Name</div>
<div class="product-name abs" style="left:343px;top:891px">Product Name</div>
<div class="product-name abs" style="left:470px;top:890px">Product Name</div>
<div class="product-name abs" style="left:594px;top:891px">Product Name</div>

<aside class="panel abs" style="left:736px;top:216px;width:185px;height:722px">
  <div class="panel-head heading" style="top:0">Little about products</div>
  <div class="panel-head heading" style="top:241px;background:linear-gradient(#262626,#0e0e0e)">Special Products</div>
</aside>
<p class="about-text abs">We at Brightweave Studio think graphic design as a combination and collaboration of ideas and technology.<br><br>Our Website Design team give an unforgettable impression on the customers and the clients. We can assure you that this is the best place for requirement of yours regarding website design solutions</p>
<div class="read-more abs">read more</div>

<div class="special abs" style="left:746px;top:508px;background:linear-gradient(90deg,#fff,#222 30%,#888 65%,#fff)" role="img" aria-label="Mobile phones"></div>
<div class="special abs" style="left:746px;top:582px;background:radial-gradient(circle at 50% 55%,#111,#444 45%,#fff 70%)" role="img" aria-label="Dance shoe"></div>
<div class="special abs" style="left:746px;top:660px;background:radial-gradient(circle at 50% 50%,#c23aa8,#e894d8 45%,#fff 70%)" role="img" aria-label="Pink media player"></div>
<div class="special abs" style="left:746px;top:738px;background:radial-gradient(circle at 50% 50%,#ddd,#111 35%,#555 55%,#fff 75%)" role="img" aria-label="Sports wristwatch"></div>
<div class="special abs" style="left:748px;top:810px;background:linear-gradient(90deg,#fff,#9ab4d8 40%,#2a4a8a 70%,#fff)" role="img" aria-label="Blood pressure monitor"></div>
<div class="abs" style="left:822px;top:506px"><div class="special-name">Product name</div><div class="special-desc">Brief description about the prodduct</div></div>
<div class="abs" style="left:824px;top:580px"><div class="special-name">Product name</div><div class="special-desc">Brief description about the prodduct</div></div>
<div class="abs" style="left:825px;top:659px"><div class="special-name">Product name</div><div class="special-desc">Brief description about the prodduct</div></div>
<div class="abs" style="left:825px;top:737px"><div class="special-name">Product name</div><div class="special-desc">Brief description about the prodduct</div></div>
<div class="abs" style="left:826px;top:808px"><div class="special-name">Product name</div><div class="special-desc">Brief description about the prodduct</div></div>

<footer class="site-footer abs"></footer>
<h2 class="heading abs" style="left:34px;top:966px">Quick Links</h2>
<ul class="quick-links abs" style="left:43px;top:1005px"><li>Home</li><li>About Pawn Shop</li><li>Services</li><li>Products</li><li>Testimonials</li></ul>
<ul class="quick-links abs" style="left:162px;top:1005px"><li>Recent News</li><li>Location</li><li>Branches</li><li>Support</li></ul>
<ul class="quick-links abs" style="left:256px;top:1005px"><li>Speical Products</li><li>Features</li><li>FAQ</li><li>Contact</li></ul>
<ul class="quick-links abs" style="left:368px;top:1005px"><li>Products</li><li>Sitemap</li><li>My Account</li></ul>
<h2 class="heading abs" style="left:516px;top:966px">Our Stores</h2>
<div class="store abs" style="left:516px;top:995px">4127 W Hollister Ave<br>Harlow Ridge, IL 60892<br>555-862-1937</div>
<div class="store abs" style="left:660px;top:993px">Brindle Cove Pawn Shop<br>2805 E Fenwick St.<br>Ferncliff, IL 60847<br>555-317-4086</div>

<div class="copyright-bar abs"></div>
<div class="copyright abs">© 2012 Compay Name<span>|</span>All right reserved</div>

</body>
</html>
```